ARC VOLLEY Business Card Project

I'd like to request a business card design for the new company I've launched.
The name of the company is "ARC VOLLEY" an indoor unmanned tennis practice facility.
We would like to see designs that use our brand identity color in the logo I've attached.
We hope to get the design with modern, luxurious and elegant tone and manner.
We hope the logo should not be too big.

Business card must have elements as below:
- Logo (One of the logos I've attached)
- Name (In Korean Text) : 박 서 윤
- Title (In Korean Text) : 대표
- Phone Number : 010-8472-3916
- Email Address : seoyun.park@arcvolley-example.co.kr
- Website : www.arcvolley-example.co.kr
- Instagram : arcvolley
- Address (In Korean text) : 경기도 용인시 수지구 풍덕천로 456 미래타워 5층 501호, 502호

Target Market(s)

Tennis amateurs in 20 to 40s

Industry/Entity Type

Sports, Hobby

Contact Information for Business Card

- Logo (One of the logos I've attached) - Name (In Korean Text) : 박 서 윤 - Title (In Korean Text) : 대표 - Phone Number : 010-8472-3916 - Email Address : seoyun.park@arcvolley-example.co.kr - Website : www.arcvolley-example.co.kr - Instagram : arcvolley - Address (In Korean text) : 경기도 용인시 수지구 풍덕천로 456 미래타워 5층 501호, 502호

Font styles to use
Sans Serif

Requirements
Must have
• Double sided
Nice to have
• Logo with intaglio or relief embossing
Should not have
• Logo should not be too big.

```html
<!DOCTYPE html>
<html lang="ko">
<head>
<meta charset="utf-8">
<title>ARC VOLLEY Business Card</title>
<link rel="stylesheet" href="https://fonts.googleapis.com/css2?family=Montserrat:wght@400;500;700&family=Noto+Sans+KR:wght@400;700&display=swap">
<style>
  :root {
    --bg: #a9aaac;
    --green-deep: #224a31;
    --green: #2e5b3f;
    --green-soft: #4b7058;
    --paper: #f1f1f0;
    --paper-shade: #e2e3e2;
    --ink: #3c3d3d;
    --white: #ffffff;
  }
  * { margin: 0; padding: 0; box-sizing: border-box; }
  html, body { width: 1200px; height: 960px; overflow: hidden; }
  body {
    background: var(--bg);
    display: flex;
    flex-direction: column;
    align-items: center;
    justify-content: center;
    gap: 44px;
    font-family: "Montserrat", sans-serif;
  }
  .card {
    position: relative;
    width: 740px;
    height: 411px;
    overflow: hidden;
    box-shadow: 0 6px 18px rgba(0,0,0,0.18);
  }

  /* Front */
  .card-front {
    background: linear-gradient(135deg, var(--white) 0%, var(--paper) 55%, var(--paper-shade) 100%);
  }
  .symbol-watermark {
    position: absolute;
    left: -60px;
    top: -40px;
    width: 300px;
    height: 300px;
    border-radius: 50%;
    background: radial-gradient(circle, rgba(46,91,63,0.06) 0%, rgba(46,91,63,0.03) 55%, rgba(46,91,63,0) 72%);
  }
  .brand-front {
    position: absolute;
    left: 300px;
    top: 78px;
    font-family: "Montserrat", sans-serif;
    font-weight: 500;
    font-size: 40px;
    letter-spacing: 2px;
    color: var(--green);
  }
  .divider {
    position: absolute;
    left: 150px;
    top: 168px;
    width: 520px;
    height: 1px;
    background: var(--green-soft);
  }
  .person {
    position: absolute;
    left: 70px;
    top: 108px;
    font-family: "Noto Sans KR", sans-serif;
    color: var(--green);
  }
  .person-name {
    font-size: 30px;
    font-weight: 700;
    letter-spacing: 4px;
    line-height: 1.1;
  }
  .person-title {
    font-size: 18px;
    font-weight: 400;
    margin-top: 4px;
  }
  .contact-list {
    position: absolute;
    right: 68px;
    top: 190px;
    list-style: none;
    text-align: right;
    color: var(--ink);
    font-size: 17px;
    line-height: 30px;
  }
  .contact-list li {
    display: flex;
    justify-content: flex-end;
    align-items: center;
    gap: 12px;
  }
  .contact-list strong { font-weight: 700; }
  .contact-icon { width: 18px; height: 18px; flex: none; }
  .address-band {
    position: absolute;
    left: 0;
    top: 336px;
    width: 100%;
    height: 54px;
    background: linear-gradient(90deg, var(--green) 0%, var(--green-deep) 100%);
    display: flex;
    align-items: center;
    padding-left: 34px;
    gap: 12px;
    color: var(--white);
    font-family: "Noto Sans KR", sans-serif;
    font-size: 19px;
    letter-spacing: 0.5px;
  }
  .pin-icon { width: 16px; height: 20px; flex: none; }

  /* Back */
  .card-back {
    display: flex;
    align-items: center;
    justify-content: center;
  }
  .back-pattern {
    position: absolute;
    inset: 0;
    background: radial-gradient(ellipse at 30% 20%, var(--green-soft) 0%, var(--green) 45%, var(--green-deep) 100%);
  }
  .brand-back {
    position: relative;
    font-family: "Montserrat", sans-serif;
    font-weight: 500;
    font-size: 40px;
    letter-spacing: 2px;
    color: var(--white);
  }
</style>
</head>
<body>

  <section class="card card-front" aria-label="Business card front">
    <div class="symbol-watermark" role="img" aria-label="Faint enlarged brand symbol watermark"></div>

    <div class="brand-front">ARC VOLLEY</div>
    <div class="divider"></div>

    <div class="person">
      <div class="person-name">박 서 윤</div>
      <div class="person-title">대표</div>
    </div>

    <ul class="contact-list">
      <li>010-8472-3916
        <svg class="contact-icon" viewBox="0 0 24 24" aria-hidden="true"><path fill="#2e5b3f" d="M6.6 10.8a15.1 15.1 0 0 0 6.6 6.6l2.2-2.2c.3-.3.7-.4 1-.2 1.1.4 2.3.6 3.6.6.6 0 1 .4 1 1V20c0 .6-.4 1-1 1A17 17 0 0 1 3 4c0-.6.4-1 1-1h3.5c.6 0 1 .4 1 1 0 1.3.2 2.5.6 3.6.1.3 0 .7-.2 1z"/></svg>
      </li>
      <li>seoyun.park@arcvolley-example.co.kr
        <svg class="contact-icon" viewBox="0 0 24 24" aria-hidden="true"><rect x="2" y="5" width="20" height="14" rx="1.5" fill="#2e5b3f"/><path d="M3 6l9 7 9-7" fill="none" stroke="#f1f1f0" stroke-width="1.6"/></svg>
      </li>
      <li><span>www.<strong>arcvolley-example</strong>.co.kr</span>
        <svg class="contact-icon" viewBox="0 0 24 24" aria-hidden="true"><circle cx="12" cy="12" r="9.5" fill="#2e5b3f"/><g fill="none" stroke="#f1f1f0" stroke-width="1.3"><ellipse cx="12" cy="12" rx="4" ry="9.5"/><path d="M2.5 12h19M4 7h16M4 17h16"/></g></svg>
      </li>
      <li>arcvolley
        <svg class="contact-icon" viewBox="0 0 24 24" aria-hidden="true"><rect x="3" y="3" width="18" height="18" fill="#2e5b3f"/></svg>
      </li>
    </ul>

    <div class="address-band">
      <svg class="pin-icon" viewBox="0 0 16 20" aria-hidden="true"><path fill="#ffffff" d="M8 0a7 7 0 0 0-7 7c0 5 7 13 7 13s7-8 7-13a7 7 0 0 0-7-7zm0 9.5A2.5 2.5 0 1 1 8 4.5a2.5 2.5 0 0 1 0 5z"/></svg>
      <span>경기도 용인시 수지구 풍덕천로 456 미래타워 5층 501호, 502호</span>
    </div>
  </section>

  <section class="card card-back" aria-label="Business card back">
    <div class="back-pattern" role="img" aria-label="Subtle repeating brand-symbol pattern on deep green"></div>
    <div class="brand-back">ARC VOLLEY</div>
  </section>

</body>
</html>
```